Coastline Haven Retreats Business Card Design

Design a business card for Coastline Haven Retreats. Look at the website for colors and reference. Card should have logo, name, title, office number, mobile number, email, URL and a tagline like, "Luxury Hotel & Resort Email Marketing" (This might change).

https://www.coastlinehavenretreats.example

The rest I will leave up to your imagination.

Contact Information for Business Card

Logo, name, title, office number, mobile number, email, URL and a tagline like, "Luxury Hotel & Resort Email Marketing" (This might change).

```html
<!DOCTYPE html>
<html lang="en">
<head>
<meta charset="utf-8">
<title>Coastline Haven Retreats – Business Card</title>
<link rel="stylesheet" href="https://fonts.googleapis.com/css2?family=Arimo:wght@400;700&display=swap">
<style>
  :root {
    --bg: #dcdcdc;
    --ink: #1a1a1a;
    --paper: #ffffff;
    --orange: #f07522;
    --card-w: 760px;
    --card-h: 434px;
  }
  * { box-sizing: border-box; margin: 0; padding: 0; }
  html, body {
    width: 1200px; height: 998px; overflow: hidden;
    background: var(--bg);
    font-family: "Arimo", Arial, sans-serif;
  }
  .canvas { position: relative; width: 1200px; height: 998px; }

  .card {
    position: absolute;
    width: var(--card-w); height: var(--card-h);
    left: 220px;
    overflow: hidden;
    box-shadow: 0 6px 18px rgba(0,0,0,.18);
  }
  .card--back { top: 48px; background: var(--ink); }
  .card--front { top: 514px; background: var(--paper); }

  /* Wordmark */
  .wordmark {
    position: absolute;
    display: flex; align-items: center; gap: 14px;
    font-weight: 700; text-transform: uppercase; white-space: nowrap;
  }
  .wordmark__square { background: var(--orange); flex: none; }
  .card--back .wordmark {
    left: 50%; top: 50%; transform: translate(-50%, -50%);
    color: var(--paper); font-size: 42px; letter-spacing: 1px;
  }
  .card--back .wordmark__square { width: 30px; height: 30px; }
  .card--front .wordmark {
    left: 40px; top: 140px;
    color: var(--ink); font-size: 18px; letter-spacing: .5px; gap: 10px;
  }
  .card--front .wordmark__square { width: 14px; height: 14px; }

  /* Front details */
  .divider {
    position: absolute; left: 380px; top: 58px;
    width: 2px; height: 186px; background: var(--orange);
  }
  .details { position: absolute; left: 400px; top: 48px; color: var(--ink); }
  .details__name {
    color: var(--orange); font-weight: 700; font-size: 24px;
    letter-spacing: .5px; text-transform: uppercase; margin-bottom: 4px;
  }
  .details__role { font-size: 15px; line-height: 21px; }
  .contact { list-style: none; margin-top: 8px; }
  .contact__item {
    display: flex; align-items: center; gap: 10px;
    font-size: 15px; line-height: 22px; white-space: nowrap;
  }
  .contact__icon { width: 14px; height: 14px; flex: none; fill: var(--orange); }

  .wave { position: absolute; left: 0; bottom: 0; width: 100%; height: 100%; }
</style>
</head>
<body>
<main class="canvas">

  <section class="card card--back" aria-label="Card back">
    <div class="wordmark">
      <span class="wordmark__square"></span>
      <span>Coastline Haven Retreats</span>
    </div>
  </section>

  <section class="card card--front" aria-label="Card front">
    <svg class="wave" viewBox="0 0 760 434" preserveAspectRatio="none" aria-hidden="true">
      <path d="M140 430 C 330 402, 440 352, 560 326 C 650 308, 710 302, 740 300"
            fill="none" stroke="#1a1a1a" stroke-width="5"/>
      <path d="M140 434 L140 432 C 330 408, 450 362, 570 336 C 660 318, 720 312, 760 310 L760 434 Z"
            fill="#f07522"/>
      <path d="M0 434 L140 434 L140 432 Z" fill="#f07522"/>
    </svg>

    <div class="wordmark">
      <span class="wordmark__square"></span>
      <span>Coastline Haven Retreats</span>
    </div>

    <div class="divider"></div>

    <div class="details">
      <h1 class="details__name">Daniel Mercer</h1>
      <p class="details__role">Co-Founder</p>
      <p class="details__role">Luxury Hotel &amp; Resort</p>
      <p class="details__role">Email Marketing</p>
      <ul class="contact">
        <li class="contact__item">
          <svg class="contact__icon" viewBox="0 0 16 16"><path d="M2 6c0-2 3-3 6-3s6 1 6 3v1h-3V6H5v1H2z M4 8h8l1 6H3z"/></svg>
          555-214-0387
        </li>
        <li class="contact__item">
          <svg class="contact__icon" viewBox="0 0 16 16"><path d="M4 1h8v14H4z M5.5 2.5v10h5v-10z"/></svg>
          555-308-6142
        </li>
        <li class="contact__item">
          <svg class="contact__icon" viewBox="0 0 16 16"><path d="M1 3h14v10H1z M2 4l6 5 6-5"/></svg>
          info@coastlinehavenretreats.example
        </li>
        <li class="contact__item">
          <svg class="contact__icon" viewBox="0 0 16 16"><circle cx="8" cy="8" r="7"/></svg>
          www.coastlinehavenretreats.example
        </li>
      </ul>
    </div>
  </section>

</main>
</body>
</html>
```